Lumo Habitat Real estate Costa del sol

we need a website for our Company based in Costa del sol, Spain. We sell properties on the spanish coast that is called costa del sol. We are concentrating on exclusive properties and would like the webdesign to show this. In our website we want to have area descriptions of the different areas we sell our Products. We will also implement a searchable database delivered by a third part where all properties for sale in Spain are listed. When looking into the designs we would like our main page to have a overview of the coast where the different areas are shown. Have a look at brightvillarow.com or mykelsa.com to see. The webpage will be presented in 4 languages, English, spanish, Swedish and norwegian, and shall of course also be prepared for social medias. We want an easy Contemporary design but still with an exclusive feeling!
Target Market(s)
Scandinavian and North european Citizens wants to buy a property in Spain
Industry/Entity Type
Real Estate
Number of Pages Required
5+ page
Look and feel

```html
<!DOCTYPE html>
<html lang="en">
<head>
<meta charset="utf-8">
<title>Lumo Habitat — Costa del Sol Properties</title>
<link href="https://fonts.googleapis.com/css2?family=Roboto:ital,wght@0,300;0,400;0,500;0,700;1,400&family=Roboto+Condensed:wght@400;700&display=swap" rel="stylesheet">
<style>
:root{
  --blue:#1a73c4;
  --blue-dark:#135a9c;
  --navy:#1c3d6b;
  --orange:#f57a12;
  --ink:#2b2b2b;
  --muted:#666;
  --light:#f4f5f6;
  --footer:#151515;
  --white:#fff;
}
*{margin:0;padding:0;box-sizing:border-box}
html,body{width:1200px;height:2844px;overflow:hidden}
body{position:relative;font-family:'Roboto',sans-serif;color:var(--ink);background:var(--white)}
.abs{position:absolute}

/* header */
.brand{left:95px;top:28px;width:190px;text-align:center}
.brand-mark{width:44px;height:44px;border:4px solid #222;margin:0 auto 6px}
.brand-name{font-size:28px;font-weight:400;color:#222;letter-spacing:.3px}
.question{left:545px;top:28px;text-align:right;width:150px}
.question p{font-size:17px;color:#333}
.question strong{display:block;font-size:17px;color:var(--blue);font-weight:500;margin-top:2px}
.phone-badge{left:698px;top:33px;width:36px;height:36px;border-radius:50%;background:var(--navy);display:flex;align-items:center;justify-content:center}
.langs{left:760px;top:42px;display:flex;gap:22px;font-size:12px;color:#444}
.lang{display:flex;align-items:center;gap:8px}
.flag{width:18px;height:12px;display:inline-block}
.nav{left:347px;top:104px;width:853px;height:44px;background:var(--blue);display:flex;align-items:center;padding-left:8px}
.nav a{color:var(--white);font-size:13px;text-decoration:none;margin:0 27px 0 20px;font-weight:500}
.nav-tab{left:330px;top:104px;width:0;height:0;border-top:44px solid transparent;border-right:17px solid var(--blue)}

/* hero */
.hero{left:0;top:148px;width:1200px;height:529px;background:linear-gradient(180deg,#8a7f8e 0%,#6c6f86 30%,#40506e 60%,#2d3d5c 100%)}
.hero-title{left:764px;top:356px;font-family:'Roboto Condensed',sans-serif;font-weight:700;color:var(--white);font-size:50px;line-height:48px}
.hero-text{left:764px;top:458px;width:360px;color:var(--white);font-size:15px;line-height:22px}
.slide-arrow{top:414px;width:34px;height:34px;border-radius:50%;background:rgba(0,0,0,.55);display:flex;align-items:center;justify-content:center}

/* search */
.search{left:0;top:677px;width:1200px;height:157px;background:var(--blue)}
.search-notch{left:586px;top:659px;width:0;height:0;border-left:18px solid transparent;border-right:18px solid transparent;border-bottom:18px solid var(--blue)}
.field{height:38px;background:var(--white);font-size:12px;font-style:italic;color:#666;padding:0 14px;display:flex;align-items:center;justify-content:space-between}
.caret{width:0;height:0;border-left:5px solid transparent;border-right:5px solid transparent;border-top:6px solid #444}
.search-btn{background:var(--orange);color:var(--white);font-style:normal;font-weight:700;justify-content:center;font-size:14px}

/* section titles */
.section-title{width:1200px;left:0;text-align:center;font-size:29px;font-weight:400;color:#222}

/* new properties */
.card{top:944px;width:237px;height:250px;background:var(--blue)}
.card-photo{width:237px;height:188px}
.card-price{position:absolute;left:72px;top:152px;width:94px;height:36px;background:var(--blue);color:var(--white);font-size:16px;display:flex;align-items:center;justify-content:center}
.card-text{color:var(--white);font-size:11px;line-height:18px;text-align:center;padding:10px 6px 0}

/* promoted */
.promo{left:0;top:1259px;width:1200px;height:464px;background:linear-gradient(180deg,#dfe3e6 0%,#c9ced2 55%,#a7acaf 100%)}
.promo-bar{left:0;top:1259px;width:1200px;height:68px;background:rgba(120,120,120,.55);color:var(--white);font-size:24px;font-weight:700;text-align:center;line-height:68px}
.promo-panel{left:402px;top:1327px;width:398px;height:396px;background:rgba(130,130,130,.78);color:var(--white);text-align:center}
.promo-panel h3{font-family:'Roboto Condensed',sans-serif;font-weight:700;font-size:28px;line-height:35px;margin-top:79px}
.promo-panel p{font-size:13.5px;line-height:21px;margin:14px 40px 0}
.promo-panel .specs{margin-top:18px;font-size:15px;line-height:21px}
.promo-panel .price{font-size:29px;font-weight:700;margin-top:12px}
.promo-arrow{top:1470px}

/* highlighted */
.hl{width:340px;height:112px}
.hl-photo{position:absolute;left:0;top:0;width:117px;height:112px}
.hl-body{position:absolute;left:136px;top:0;width:200px}
.hl-body h4{font-size:16px;font-weight:400;color:#222}
.hl-body .hl-price{font-size:16px;color:var(--blue);margin:8px 0 6px}
.hl-body p{font-size:12px;line-height:19px;color:#555}

/* news */
.news-band{left:0;top:2161px;width:1200px;height:357px;background:var(--light)}
.news-title{left:97px;top:2193px;font-size:25px;font-weight:400;color:#222}
.testi-title{left:784px;top:2201px;font-size:19px;font-weight:400;color:#333}
.news{top:2270px;width:290px}
.news h4{font-size:17px;font-weight:400;color:#333;padding-bottom:10px}
.news .date{color:var(--orange);font-size:16px;margin-bottom:14px}
.news p{font-size:12px;line-height:20px;color:#555}
.news .more{margin-top:26px;padding-top:8px;border-top:1px solid #ddd;font-size:12px;color:#444;display:flex;align-items:center;gap:6px}
.testimonial{left:781px;top:2249px;width:320px;height:178px;background:var(--orange);color:var(--white);padding:20px 20px;font-style:italic;font-size:11px;line-height:20px;text-align:center}
.testimonial .who{margin-top:8px;text-align:right;padding-right:58px;line-height:19px;font-size:12.5px}
.avatar{left:808px;top:2392px;width:82px;height:82px;border-radius:50%;background:linear-gradient(180deg,#9a8e84,#5e6a75);border:3px solid var(--white)}

/* footer */
.footer{left:0;top:2518px;width:1200px;height:273px;background:linear-gradient(180deg,#1d1d1d,#0e0e0e)}
.foot-brand{left:95px;top:2583px;width:190px;text-align:center;color:var(--white)}
.foot-brand .brand-mark{border-color:var(--white)}
.foot-brand .brand-name{color:var(--white)}
.socials{display:flex;gap:6px;justify-content:center;margin-top:10px}
.socials span{width:22px;height:22px;border:1.5px solid #ccc;border-radius:50%}
.foot-col{top:2575px;color:var(--white)}
.foot-col h5{font-size:15px;font-weight:500;margin-bottom:14px;letter-spacing:.2px}
.foot-col p,.foot-col li{font-size:12.5px;line-height:24px;list-style:none}
.contact-line{display:flex;align-items:center;gap:16px;margin-top:12px}
.email-input{width:228px;height:40px;background:var(--white);color:#444;font-size:11px;padding:0 12px;display:flex;align-items:center;margin-top:14px}
.subscribe{display:inline-block;margin-top:16px;background:var(--blue);color:var(--white);font-size:12px;padding:10px 12px}
.copyright{left:0;top:2791px;width:1200px;height:53px;background:var(--blue);color:var(--white);font-size:12px;text-align:center;line-height:53px}
</style>
</head>
<body>

<header>
  <div class="abs brand"><div class="brand-mark"></div><div class="brand-name">Lumo Habitat</div></div>
  <div class="abs question"><p>Have any Question?</p><strong>+34 600 218 447</strong></div>
  <div class="abs phone-badge">
    <svg width="18" height="18" viewBox="0 0 24 24"><path fill="#fff" d="M6.6 10.8a15 15 0 0 0 6.6 6.6l2.2-2.2c.3-.3.7-.4 1-.2 1.1.4 2.3.6 3.6.6.6 0 1 .4 1 1V20c0 .6-.4 1-1 1A17 17 0 0 1 3 4c0-.6.4-1 1-1h3.5c.6 0 1 .4 1 1 0 1.300.2 2.500.6 3.600.1.300 0 .7-.2 1z"/></svg>
  </div>
  <div class="abs langs">
    <span class="lang"><span class="flag" style="background:#2b3f86"></span>ENGLISH</span>
    <span class="lang"><span class="flag" style="background:linear-gradient(#c60b1e 25%,#ffc400 25% 75%,#c60b1e 75%)"></span>SPANISH</span>
    <span class="lang"><span class="flag" style="background:linear-gradient(90deg,#006aa7 30%,#fecc00 30% 45%,#006aa7 45%)"></span>SWEDISH</span>
    <span class="lang"><span class="flag" style="background:linear-gradient(90deg,#ba0c2f 30%,#00205b 30% 45%,#ba0c2f 45%)"></span>NORWEGIAN</span>
  </div>
  <div class="abs nav-tab"></div>
  <nav class="abs nav">
    <a>HOMES</a><a>ABOUT US</a><a>COSTA DEL SOL</a><a>SERVICES</a><a>PROPERTIES</a><a>BLOG</a><a>CONTACT US</a>
  </nav>
</header>

<section>
  <div class="abs hero" role="img" aria-label="Evening view over a harbour town on the Costa del Sol with boats and hillside houses"></div>
  <h1 class="abs hero-title">LUMO HABITAT<br>PROPERTIES</h1>
  <p class="abs hero-text">Lorem ipsum dolor sit amet, consectetur adipiscing sed do eiusmod tempor incididunt ut labore</p>
  <div class="abs slide-arrow" style="left:32px"><svg width="12" height="14" viewBox="0 0 12 14"><path d="M9 1 3 7l6 6" stroke="#fff" stroke-width="2.5" fill="none"/></svg></div>
  <div class="abs slide-arrow" style="left:1130px"><svg width="12" height="14" viewBox="0 0 12 14"><path d="m3 1 6 6-6 6" stroke="#fff" stroke-width="2.5" fill="none"/></svg></div>
</section>

<section>
  <div class="abs search-notch"></div>
  <div class="abs search"></div>
  <div class="abs field" style="left:140px;top:713px;width:224px">Select one or more locations<span class="caret"></span></div>
  <div class="abs field" style="left:372px;top:713px;width:223px">All Types<span class="caret"></span></div>
  <div class="abs field" style="left:603px;top:713px;width:224px">Min price<span class="caret"></span></div>
  <div class="abs field" style="left:834px;top:713px;width:224px">Phone No</div>
  <div class="abs field" style="left:140px;top:760px;width:224px">Min beds<span class="caret"></span></div>
  <div class="abs field" style="left:372px;top:760px;width:223px">subtype<span class="caret"></span></div>
  <div class="abs field" style="left:603px;top:760px;width:224px">Unlimited<span class="caret"></span></div>
  <div class="abs field search-btn" style="left:834px;top:760px;width:224px">SEARCH &#8853;</div>
</section>

<section>
  <h2 class="abs section-title" style="top:868px">NEW PROPERTIES</h2>
  <div class="abs card" style="left:99px"><div class="card-photo" role="img" aria-label="Modern villa with pool at dusk" style="background:linear-gradient(180deg,#7fa6cc,#d9c6a3 60%,#4d8fb6)"></div><span class="card-price">265.000 €</span><p class="card-text">Lorem ipsum dolor sit amet, consectetur adipiscing elit, sed do eiusmod</p></div>
  <div class="abs card" style="left:353px"><div class="card-photo" role="img" aria-label="Contemporary house with lit terrace" style="background:linear-gradient(180deg,#5a6f86,#c9a56a 55%,#3b4b57)"></div><span class="card-price">265.000 €</span><p class="card-text">Lorem ipsum dolor sit amet, consectetur adipiscing elit, sed do eiusmod</p></div>
  <div class="abs card" style="left:607px"><div class="card-photo" role="img" aria-label="White cubic villa with pool" style="background:linear-gradient(180deg,#9bb7d3,#e8ecee 50%,#5aa0c4)"></div><span class="card-price">265.000 €</span><p class="card-text">Lorem ipsum dolor sit amet, consectetur adipiscing elit, sed do eiusmod</p></div>
  <div class="abs card" style="left:863px"><div class="card-photo" role="img" aria-label="Villa by the pool at twilight" style="background:linear-gradient(180deg,#2c3f6a,#a07654 55%,#2a6f9a)"></div><span class="card-price">265.000 €</span><p class="card-text">Lorem ipsum dolor sit amet, consectetur adipiscing elit, sed do eiusmod</p></div>
</section>

<section>
  <div class="abs promo" role="img" aria-label="Bright villa living room with sofas and sea view through tall windows"></div>
  <div class="abs promo-bar">SPECIALLY PROMOTED</div>
  <div class="abs promo-panel">
    <h3>4 BED DETACHED<br>VILLA IN LAS CHAPAS</h3>
    <p>Sed ut perspiciatis unde omnis iste natus error sit voluptatem accusantium doloremque laudantium, totam rem aperiam, eaque ipsa quae</p>
    <div class="specs">beds 4 // baths 6<br>built 255m2 // plot 525m2</div>
    <div class="price">1.100.000 €</div>
  </div>
  <svg class="abs promo-arrow" style="left:28px" width="20" height="44" viewBox="0 0 20 44"><path d="M18 2 2 22l16 20" stroke="#fff" stroke-width="2" fill="none"/></svg>
  <svg class="abs promo-arrow" style="left:1152px" width="20" height="44" viewBox="0 0 20 44"><path d="m2 2 16 20L2 42" stroke="#fff" stroke-width="2" fill="none"/></svg>
</section>

<section>
  <h2 class="abs section-title" style="top:1757px;font-size:24px">HIGHLIGHTED PROPERTIES</h2>
  <div class="abs hl" style="left:99px;top:1828px"><div class="hl-photo" role="img" aria-label="Beach house on stilts" style="background:linear-gradient(180deg,#8fb8df,#7fb8a6 60%,#c9b48e)"></div><div class="hl-body"><h4>Sed ut perspiciatis unde</h4><div class="hl-price">265.000 €</div><p>Lorem ipsum dolor sit amet, consectetur adipiscing elit, sed do eiusmod</p></div></div>
  <div class="abs hl" style="left:449px;top:1828px"><div class="hl-photo" role="img" aria-label="Two storey family house" style="background:linear-gradient(180deg,#a9c6e4,#c2b39c 60%,#6f7a55)"></div><div class="hl-body"><h4>Sed ut perspiciatis unde</h4><div class="hl-price">265.000 €</div><p>Lorem ipsum dolor sit amet, consectetur adipiscing elit, sed do eiusmod</p></div></div>
  <div class="abs hl" style="left:800px;top:1828px"><div class="hl-photo" role="img" aria-label="Wooden beach house" style="background:linear-gradient(180deg,#9dbfe0,#b88a5c 60%,#d8c6a0)"></div><div class="hl-body"><h4>Sed ut perspiciatis unde</h4><div class="hl-price">265.000 €</div><p>Lorem ipsum dolor sit amet, consectetur adipiscing elit, sed do eiusmod</p></div></div>
  <div class="abs hl" style="left:99px;top:1981px"><div class="hl-photo" role="img" aria-label="Modern house facing the sea" style="background:linear-gradient(180deg,#cfe2f2,#5fa8d3 60%,#e4e4e0)"></div><div class="hl-body"><h4>Sed ut perspiciatis unde</h4><div class="hl-price">265.000 €</div><p>Lorem ipsum dolor sit amet, consectetur adipiscing elit, sed do eiusmod</p></div></div>
  <div class="abs hl" style="left:449px;top:1981px"><div class="hl-photo" role="img" aria-label="Villa with infinity pool" style="background:linear-gradient(180deg,#7a8fa3,#cfd4d4 55%,#3c8fb8)"></div><div class="hl-body"><h4>Sed ut perspiciatis unde</h4><div class="hl-price">265.000 €</div><p>Lorem ipsum dolor sit amet, consectetur adipiscing elit, sed do eiusmod</p></div></div>
  <div class="abs hl" style="left:800px;top:1981px"><div class="hl-photo" role="img" aria-label="Thatched bungalow over turquoise water" style="background:linear-gradient(180deg,#7fc4e6,#8a6a4a 50%,#3fc0c9)"></div><div class="hl-body"><h4>Sed ut perspiciatis unde</h4><div class="hl-price">265.000 €</div><p>Lorem ipsum dolor sit amet, consectetur adipiscing elit, sed do eiusmod</p></div></div>
</section>

<section>
  <div class="abs news-band"></div>
  <h2 class="abs news-title">LATEST NEWS</h2>
  <h2 class="abs testi-title">TESTIMONIAL</h2>
  <article class="abs news" style="left:97px">
    <h4>Nemo Enim Ipsam Voluptatem ?</h4>
    <div class="date">Janu 21, 2016</div>
    <p>Duis aute irure dolor in reprehenderit in voluptate velit esse cillum dolore eu fugiat nulla pariatur. Excepteur sint occaecat cupidatat non proident, sunt in culpa qui officia deserunt mollit</p>
    <div class="more"><svg width="11" height="11" viewBox="0 0 12 12"><circle cx="6" cy="6" r="5" stroke="#444" fill="none" stroke-width="1.4"/><path d="M6 3v3h2" stroke="#444" stroke-width="1.4" fill="none"/></svg>READ MORE</div>
  </article>
  <article class="abs news" style="left:449px">
    <h4>Nemo Enim Ipsam Voluptatem ?</h4>
    <div class="date">Janu 21, 2016</div>
    <p>Duis aute irure dolor in reprehenderit in voluptate velit esse cillum dolore eu fugiat nulla pariatur. Excepteur sint occaecat cupidatat non proident, sunt in culpa qui officia deserunt mollit</p>
    <div class="more"><svg width="11" height="11" viewBox="0 0 12 12"><circle cx="6" cy="6" r="5" stroke="#444" fill="none" stroke-width="1.4"/><path d="M6 3v3h2" stroke="#444" stroke-width="1.4" fill="none"/></svg>READ MORE</div>
  </article>
  <blockquote class="abs testimonial">
    " Duis aute irure dolor in reprehenderit in voluptate velit esse cillum dolore eu fugiat nulla pariatur. Excepteur sint occaecat cupidatat non proident, sunt in culpa qui officia deserunt mollit anim id est laborum."
    <div class="who">- MAREN SOLVIK<br>Property Agent .</div>
  </blockquote>
  <div class="abs avatar" role="img" aria-label="Portrait of the reviewing property agent"></div>
</section>

<footer>
  <div class="abs footer"></div>
  <div class="abs foot-brand"><div class="brand-mark"></div><div class="brand-name">Lumo Habitat</div>
    <div class="socials"><span></span><span></span><span></span><span></span><span></span></div></div>
  <div class="abs foot-col" style="left:385px">
    <h5>CONTACT US</h5>
    <p>Lumo Habitat<br>29604 Calle Brisa 12 Marbella Spain</p>
    <div class="contact-line"><svg width="16" height="16" viewBox="0 0 24 24"><path fill="none" stroke="#fff" stroke-width="1.8" d="M6.6 10.8a15 15 0 0 0 6.6 6.6l2.2-2.2c.3-.3.7-.4 1-.2 1.1.4 2.3.6 3.6.6.6 0 1 .4 1 1V20c0 .6-.4 1-1 1A17 17 0 0 1 3 4c0-.6.4-1 1-1h3.5c.6 0 1 .4 1 1 0 1.3.2 2.5.6 3.6.1.3 0 .7-.2 1z"/></svg><p>+34 952 407 316</p></div>
    <div class="contact-line" style="margin-top:4px"><svg width="16" height="12" viewBox="0 0 16 12"><rect x="1" y="1" width="14" height="10" fill="none" stroke="#fff" stroke-width="1.4"/><path d="m1 1 7 6 7-6" fill="none" stroke="#fff" stroke-width="1.4"/></svg><p>info@lumohabitat.com</p></div>
  </div>
  <div class="abs foot-col" style="left:697px">
    <h5>QUICK LINKS</h5>
    <ul><li>Home</li><li>About Us</li><li>Property</li><li>Agent</li><li>Contact Us</li></ul>
  </div>
  <div class="abs foot-col" style="left:874px;width:230px">
    <h5>SIGN UP TO RECEIVE EMAIL</h5>
    <p style="line-height:20px">Excepteur sint occaecat cupidatat non proident, sunt in culpa qui</p>
    <div class="email-input">Enter email</div>
    <span class="subscribe">SUBSCRIBE</span>
  </div>
  <div class="abs copyright">Copyright©2016 Lumo Habitat .All Right Reserved</div>
</footer>

</body>
</html>
```